Vantor Medica Innovative Business Card

Stunning business card. Background will be black. Letters in gold. Modern yet simple design that is attention grabbing. QR code leading to site. Attractive primarily to males ages 30 to 50 but also to females in same age range looking for beauty and mental health products

Target Market(s)

Males in the 30-50 age demographics

Industry/Entity Type

Pharmaceuticals selling erectile dysfunction and mens health medications

Contact Information for Business Card

www.vantormedica.example; (775) BUY-KELO; info@vantormedica.example

Colors
FFC000
F8CF3A
FAE287
FDF2CF
FEFAEE

Requirements
Must have
• Black business card with gold letters.
Nice to have
• perhaps just the logo or the "R" icon by itself on one side
Should not have
• too much content so it does not look busy

```html
<!DOCTYPE html>
<html lang="en">
<head>
<meta charset="utf-8">
<title>Vantor Medica Business Card</title>
<link href="https://fonts.googleapis.com/css2?family=Montserrat:wght@400;500;700&display=swap" rel="stylesheet">
<style>
  :root {
    --stage: #141414;
    --card: #1c1c1c;
    --card-edge: #262626;
    --gold: #d9a93a;
    --gold-light: #f8cf3a;
    --gold-soft: #fae287;
  }
  * { margin: 0; padding: 0; box-sizing: border-box; }
  html, body {
    width: 1200px;
    height: 900px;
    overflow: hidden;
    background: var(--stage);
    font-family: "Montserrat", sans-serif;
  }
  .stage {
    width: 1200px;
    height: 900px;
    display: flex;
    flex-direction: column;
    align-items: center;
    justify-content: center;
    gap: 44px;
  }
  .card {
    width: 630px;
    height: 360px;
    background: linear-gradient(135deg, var(--card) 0%, #202020 60%, #191919 100%);
    border: 1px solid var(--card-edge);
    box-shadow: 0 18px 40px rgba(0, 0, 0, 0.6);
    position: relative;
  }
  .card-front {
    display: flex;
    align-items: center;
    justify-content: center;
  }
  .brand {
    display: flex;
    align-items: center;
    gap: 14px;
    color: var(--gold);
    font-weight: 700;
    text-transform: uppercase;
    letter-spacing: 0.04em;
  }
  .brand-dot {
    border-radius: 50%;
    background: var(--gold);
    flex: none;
  }
  .card-front .brand { font-size: 34px; }
  .card-front .brand-dot { width: 46px; height: 46px; }

  .card-back {
    display: flex;
    align-items: center;
    padding: 0 48px;
  }
  .card-back .brand {
    font-size: 22px;
    width: 230px;
    flex-wrap: wrap;
    gap: 10px;
  }
  .card-back .brand-dot { width: 30px; height: 30px; }
  .divider {
    width: 2px;
    height: 140px;
    background: var(--gold);
    margin: 0 38px 0 18px;
    flex: none;
  }
  .contact { color: var(--gold); }
  .contact-name {
    font-size: 25px;
    font-weight: 700;
    color: var(--gold-light);
    letter-spacing: 0.02em;
    text-transform: uppercase;
    line-height: 1;
  }
  .contact-role {
    font-size: 15px;
    font-weight: 500;
    letter-spacing: 0.06em;
    text-transform: uppercase;
    margin: 4px 0 20px;
  }
  .contact-list { list-style: none; }
  .contact-list li {
    display: flex;
    align-items: center;
    gap: 8px;
    font-size: 16px;
    font-weight: 500;
    line-height: 1.55;
  }
  .contact-list svg { width: 12px; height: 12px; flex: none; }
</style>
</head>
<body>
<main class="stage">
  <section class="card card-front">
    <div class="brand">
      <span class="brand-dot"></span>
      <span class="brand-name">Vantor Medica</span>
    </div>
  </section>

  <section class="card card-back">
    <div class="brand">
      <span class="brand-dot"></span>
      <span class="brand-name">Vantor Medica</span>
    </div>
    <span class="divider"></span>
    <div class="contact">
      <p class="contact-name">Daniel Hartwell</p>
      <p class="contact-role">Director</p>
      <ul class="contact-list">
        <li>
          <svg viewBox="0 0 12 12" fill="none" stroke="#d9a93a" stroke-width="1.4"><path d="M3 1 L5 3.5 L3.8 4.8 Q5 7.5 7.2 8.2 L8.5 7 L11 9 L9.5 11 Q3 10 1 2.5 Z"/></svg>
          (775) BUY-KELO
        </li>
        <li>
          <svg viewBox="0 0 12 12" fill="none" stroke="#d9a93a" stroke-width="1.3"><rect x="1" y="2.5" width="10" height="7"/><path d="M1 2.5 L6 6.5 L11 2.5"/></svg>
          info@vantormedica.example
        </li>
        <li>
          <svg viewBox="0 0 12 12" fill="none" stroke="#d9a93a" stroke-width="1.1"><circle cx="6" cy="6" r="5"/><ellipse cx="6" cy="6" rx="2.2" ry="5"/><path d="M1 6 H11"/></svg>
          www.vantormedica.example
        </li>
      </ul>
    </div>
  </section>
</main>
</body>
</html>
```